Justizthriller  sucht eBook-Cover
Justizthriller sucht eBook-Cover
Bin sehr zufrieden. Alle Fragen und Wünsche wurden sehr schnell bearbeitet. Sehr freundlicher Designer. Kann ich nur empfehlen.
Zielgruppe
Wir möchten unseren Roman als e-book verkaufen. Unsere Zielgruppe sind alle Leute die sich für Justizthriller und Krimis und Tatsachenromane interessieren.
Aufgabenstellung
Eigentlich hat uns die alte Vorlage gefallen. Freuen uns aber für neue Ideen. Wichtig natürlich, dass das Cover sofort auffällt. Hätte gerne, dass auf der Krawatte lauter kleine 'Justizia' Aufdrucke drauf kommen.
Wichtig ist noch der Zusatz auf der Vorderseite: 'Nach einer wahren Begebenheit'
Und 72 ppi-ebooks , 1800 x 2500 px soll auch verwendet werden.

```html
<!DOCTYPE html>
<html lang="de">
<head>
<meta charset="utf-8">
<title>Grünes Indiz Akte! – eBook-Cover</title>
<link rel="stylesheet" href="https://fonts.googleapis.com/css2?family=Special+Elite&family=Open+Sans:wght@700&display=swap">
<style>
  :root {
    --folder-dark: #3f3f3f;
    --folder-mid: #575757;
    --folder-light: #626262;
    --stamp-white: #f2f2f2;
    --accent-yellow: #f6b500;
    --rule-dark: #2a2a2a;
    --cord: #1e1e1e;
    --eyelet: #9a9a9a;
    --photo-red: #c8321e;
    --photo-green: #4f8a2a;
    --photo-skin: #e9c3a8;
  }
  * { margin: 0; padding: 0; box-sizing: border-box; }
  html, body { width: 864px; height: 1200px; overflow: hidden; background: var(--folder-dark); }
  .cover {
    position: relative;
    width: 864px;
    height: 1200px;
    overflow: hidden;
    background: radial-gradient(ellipse at 55% 35%, var(--folder-light) 0%, var(--folder-mid) 45%, var(--folder-dark) 100%);
  }
  .folder-art { position: absolute; inset: 0; }
  .authors {
    position: absolute;
    top: 20px;
    left: 0;
    width: 864px;
    text-align: center;
    font-family: "Open Sans", sans-serif;
    font-weight: 700;
    font-size: 27px;
    line-height: 38px;
    color: var(--accent-yellow);
  }
  .title-stamp {
    position: absolute;
    left: 152px;
    top: 72px;
    width: 562px;
    height: 410px;
    border: 4px solid var(--stamp-white);
    display: flex;
    justify-content: center;
    align-items: center;
  }
  .title-stamp h1 {
    font-family: "Special Elite", monospace;
    font-weight: 400;
    font-size: 118px;
    line-height: 124px;
    letter-spacing: 2px;
    color: var(--stamp-white);
    text-align: center;
    white-space: nowrap;
  }
  .subtitle {
    position: absolute;
    top: 494px;
    left: 0;
    width: 864px;
    text-align: center;
    font-family: "Open Sans", sans-serif;
    font-weight: 700;
    font-size: 35px;
    line-height: 46px;
    color: var(--accent-yellow);
  }
  .hero-photo {
    position: absolute;
    left: 155px;
    top: 600px;
    width: 500px;
    height: 490px;
    border-radius: 40px 140px 60px 120px;
    background:
      radial-gradient(circle at 70% 15%, var(--photo-green) 0%, var(--photo-green) 22%, transparent 40%),
      radial-gradient(circle at 45% 65%, var(--photo-red) 0%, var(--photo-red) 35%, transparent 60%),
      linear-gradient(160deg, var(--photo-skin) 0%, #c98e73 100%);
    opacity: 0.95;
  }
  .tagline {
    position: absolute;
    bottom: 22px;
    left: 0;
    width: 864px;
    text-align: center;
    font-family: "Special Elite", monospace;
    font-size: 33px;
    line-height: 40px;
    color: var(--stamp-white);
    letter-spacing: 1px;
    white-space: nowrap;
  }
</style>
</head>
<body>
<main class="cover">
  <svg class="folder-art" width="864" height="1200" viewBox="0 0 864 1200" aria-hidden="true">
    <g class="folder-rules" stroke="var(--rule-dark)" stroke-width="2">
      <line x1="370" y1="170" x2="864" y2="170"/>
      <line x1="370" y1="246" x2="864" y2="246"/>
      <line x1="370" y1="326" x2="864" y2="326"/>
    </g>
    <g class="binding-cord">
      <path d="M54 160 C50 300 62 450 52 600 C50 640 54 670 58 690" fill="none" stroke="var(--cord)" stroke-width="9" stroke-linecap="round"/>
      <path d="M54 160 C50 300 62 450 52 600 C50 640 54 670 58 690" fill="none" stroke="#6a6a6a" stroke-width="2" stroke-dasharray="3 5"/>
      <circle class="eyelet" cx="53" cy="150" r="13" fill="var(--eyelet)"/>
      <circle cx="53" cy="150" r="7" fill="var(--cord)"/>
      <circle class="eyelet" cx="59" cy="690" r="13" fill="var(--eyelet)"/>
      <circle cx="59" cy="690" r="7" fill="var(--cord)"/>
    </g>
  </svg>

  <p class="authors">Jonas Reiber &amp; Britta Olmen</p>

  <div class="title-stamp">
    <h1>GRÜNES<br>INDIZ<br>AKTE!</h1>
  </div>

  <p class="subtitle">Ein Justizthriller über<br>vegetarischen Sex</p>

  <div class="hero-photo" role="img" aria-label="Foto: Hand mit rot lackierten Nägeln hält eine Gurke über zwei Tomaten, auf einer Tomate eine kleine Justitia-Figur"></div>

  <p class="tagline">Nach einer wahren Begebenheit</p>
</main>
</body>
</html>
```